Business card design for counselling and psychotherapy practice

I am seeking a business card for a new venture into private practice. I am based in Brisbane Qld Australia. I provide holistic counselling and psychotherapy to individuals and groups.
Some words that describe the underpinnings of this practice would include: being, becoming, awareness, wholeness, contact, safety, acceptance, relationship, gestalt, paradox, interconnected, nature, process.
I would like to see designs that include earth colours.
The overall design should communicate safety and a curiosity of being and becoming.
Target Market(s)
this design is marketed toward women, professionals, lesbian, transgender, mothers
Industry/Entity Type
Safety
Contact Information for Business Card
Willow & Tide
Counselling and Psychotherapy
Maren Olcott
ph: 0417382905
email: maren.willow&tide@quietmail.net
www.willow&tidecounselling&psychotherapy.net
Logo styles of interest
Abstract Logo
Look and feel
Each slider illustrates characteristics of the customer's brand and the style your logo design should communicate.

```html
<!DOCTYPE html>
<html lang="en">
<head>
<meta charset="utf-8">
<title>Willow &amp; Tide — Business Card</title>
<link rel="stylesheet" href="https://fonts.googleapis.com/css2?family=Open+Sans:wght@700&family=Arimo:wght@400&display=swap">
<style>
  :root {
    --page: #ffffff;
    --card: #ffffff;
    --card-edge: #1a1a1a;
    --brand-green: #21a345;
    --lime: #8cc224;
    --ocean: #0079c1;
    --ink-light: #ffffff;
  }
  * { margin: 0; padding: 0; box-sizing: border-box; }
  html, body {
    width: 1200px;
    height: 999px;
    overflow: hidden;
    background: var(--page);
  }
  .business-card {
    position: absolute;
    left: 107px;
    top: 228px;
    width: 985px;
    height: 537px;
    background: var(--card);
    border: 1px solid var(--card-edge);
    overflow: hidden;
  }
  .footer-band {
    position: absolute;
    left: 0;
    right: 0;
    top: 290px;
    bottom: 0;
    background: linear-gradient(180deg, var(--lime) 0%, var(--brand-green) 12%, var(--ocean) 38%, var(--ocean) 100%);
  }
  .brand-mark {
    position: absolute;
    left: 33px;
    top: 22px;
    width: 180px;
    height: 180px;
    border-radius: 50%;
    background: var(--brand-green);
  }
  .brand-name {
    position: absolute;
    left: 240px;
    top: 35px;
    font-family: "Open Sans", Arial, sans-serif;
    font-weight: 700;
    font-size: 87px;
    line-height: 1;
    letter-spacing: 0;
    color: var(--brand-green);
    text-transform: uppercase;
    white-space: nowrap;
  }
  .brand-tagline {
    position: absolute;
    left: 280px;
    top: 128px;
    font-family: "Arimo", Arial, sans-serif;
    font-size: 19px;
    letter-spacing: 10px;
    color: var(--brand-green);
    white-space: nowrap;
  }
  .contact-block {
    position: absolute;
    right: 70px;
    top: 336px;
    text-align: right;
    font-family: "Arimo", Arial, sans-serif;
    color: var(--ink-light);
  }
  .contact-name {
    font-size: 40px;
    line-height: 54px;
    text-decoration: underline;
    text-decoration-thickness: 2px;
    text-underline-offset: 6px;
    margin-bottom: 14px;
  }
  .contact-line {
    display: flex;
    justify-content: flex-end;
    align-items: center;
    font-size: 30px;
    line-height: 35px;
    position: relative;
  }
  .contact-icon {
    position: absolute;
    right: -44px;
    width: 28px;
    height: 28px;
  }
</style>
</head>
<body>
  <section class="business-card">
    <div class="footer-band" role="img" aria-label="Flowing wave band in lime, green and ocean blue"></div>

    <div class="brand-mark"></div>
    <h1 class="brand-name">Willow&amp;Tide</h1>
    <p class="brand-tagline">Counselling and Psychotherapy</p>

    <div class="contact-block">
      <p class="contact-name">Maren Olcott</p>
      <p class="contact-line">0417382905
        <svg class="contact-icon" viewBox="0 0 28 28" aria-hidden="true">
          <path d="M10 5 C7 9 7 17 12 22 C14 24 17 24 18 22 L16 19 C14 20 13 19 12 17 C11 14 11 12 12 10 C14 10 15 9 14 7 Z" fill="var(--lime)"/>
        </svg>
      </p>
      <p class="contact-line">maren.willow&amp;tide@quietmail.net
        <svg class="contact-icon" viewBox="0 0 28 28" aria-hidden="true">
          <rect x="3" y="7" width="22" height="16" rx="2" fill="var(--lime)"/>
          <path d="M3 8 L14 16 L25 8" fill="none" stroke="var(--ocean)" stroke-width="1.5"/>
        </svg>
      </p>
      <p class="contact-line">www.willow&amp;tidecounselling&amp;psychotherapy.net
        <svg class="contact-icon" viewBox="0 0 28 28" aria-hidden="true">
          <g fill="none" stroke="var(--lime)" stroke-width="1.5">
            <circle cx="14" cy="14" r="11"/>
            <ellipse cx="14" cy="14" rx="5" ry="11"/>
            <line x1="3" y1="14" x2="25" y2="14"/>
            <line x1="5" y1="8.5" x2="23" y2="8.5"/>
            <line x1="5" y1="19.5" x2="23" y2="19.5"/>
          </g>
        </svg>
      </p>
    </div>
  </section>
</body>
</html>
```